labels on the supplement bottle

put my brand name on the table "Verdanta"
put product name 1
"MORNING CORE MATERNA
–WITH PROBIOTICS–"
put product name 2
"Vitamin D3+ Quercetinol"
put product name 3
"mane focus “
put the advert word that you create for these products
design the green area.
Updates
the product name change to
" Morning Core Materna & Aftercare“
"mane focus" change to "Shine, renewal, Blooming"
underneath the brand add small words "Your secret beauty ingredients"

```html
<!DOCTYPE html>
<html lang="en">
<head>
<meta charset="utf-8">
<title>Verdanta Supplement Labels</title>
<link href="https://fonts.googleapis.com/css2?family=Baloo+2:wght@800&family=Oswald:wght@500;600&family=Roboto+Condensed:wght@400;700&display=swap" rel="stylesheet">
<style>
  :root{
    --bg:#cfcdce;
    --white:#ffffff;
    --ink:#2e2e2e;
    --grey-text:#555555;
    --red:#c8242f;
    --orange:#f3a23a;
    --orange-soft:#f7c070;
    --green:#8cc63f;
    --green-soft:#b9de86;
    --green-dark:#5fa82b;
    --panel-line:#9a9a9a;
    --badge:#3a3a3a;
  }
  *{box-sizing:border-box;margin:0;padding:0}
  html,body{width:1200px;height:1200px;overflow:hidden}
  body{background:var(--bg);font-family:"Roboto Condensed",Arial,sans-serif;color:var(--ink);position:relative}

  .label{position:absolute;top:320px;height:560px;background:var(--white);overflow:hidden;display:flex}
  .label--bone{left:20px;width:330px}
  .label--hair{left:370px;width:395px}
  .label--prenatal{left:785px;width:395px}

  .front{position:relative;flex:1;height:100%;display:flex;flex-direction:column;align-items:center;text-align:center}
  .front > .layer{position:relative;z-index:1}

  .top-band{width:100%;height:110px;display:flex;flex-direction:column;align-items:center;justify-content:center}
  .label--bone .top-band{background:var(--red)}
  .label--hair .top-band{background:var(--green)}
  .label--prenatal .top-band{background:var(--orange);align-items:flex-start;padding-left:22px;text-align:left}

  .product-line{font-family:"Oswald",sans-serif;font-weight:500;color:var(--white);font-size:23px;letter-spacing:.3px}
  .label--hair .product-line{font-size:34px;font-weight:600;line-height:1.1}
  .advert-line{font-family:"Oswald",sans-serif;font-weight:500;color:var(--white);font-size:17px;letter-spacing:.5px;margin-top:2px}

  .partner-mark{font-family:"Oswald",sans-serif;font-weight:600;color:var(--red);font-size:24px}
  .partner-note{font-size:10px;color:var(--ink);line-height:1.2;margin-top:2px}

  .brand{margin-top:24px}
  .brand-name{font-family:"Baloo 2",sans-serif;font-weight:800;font-size:54px;line-height:1;color:var(--red)}
  .tagline{font-size:13px;font-style:normal;color:var(--grey-text);letter-spacing:.5px;margin-top:2px}

  .title{font-weight:700;font-size:22px;line-height:1.15;color:var(--ink);margin-top:12px;letter-spacing:.3px}
  .label--prenatal .title{font-weight:400;color:var(--grey-text)}
  .subtitle{font-size:13px;letter-spacing:1px;color:var(--ink);margin-top:3px}
  .label--prenatal .subtitle{color:var(--grey-text)}

  .claims{font-size:12px;color:var(--orange);margin-top:9px;letter-spacing:.3px}
  .label--prenatal .claims{font-size:14px}
  .for-whom{font-size:17px;color:var(--green-dark);margin-top:10px}

  .pill{display:inline-block;margin-top:9px;padding:2px 12px;border-radius:9px;font-size:10px;font-weight:700;color:var(--white);background:var(--red)}
  .label--hair .pill{background:var(--green)}

  .hair-claim{font-size:17px;line-height:1.25;color:var(--ink);margin-top:14px;padding:0 16px}
  .bone-claim{font-family:"Oswald",sans-serif;font-weight:500;font-size:13px;line-height:1.35;color:var(--ink);margin-top:12px;padding:0 20px}
  .diet{font-weight:700;font-size:17px;margin-top:14px}
  .label--prenatal .diet{font-weight:400;font-size:16px}

  .base-wash{position:absolute;left:0;right:0;bottom:0;height:150px;z-index:0}
  .label--bone .base-wash{background:linear-gradient(to bottom,rgba(243,162,58,0) 0%,var(--orange-soft) 55%,var(--orange) 100%)}
  .label--hair .base-wash{background:linear-gradient(to bottom,rgba(140,198,63,0) 0%,var(--green-soft) 55%,var(--green) 100%)}
  .label--prenatal .front{background:linear-gradient(to bottom,#f4f4f4 0%,#e6e6e6 100%)}
  .label--prenatal .base-wash{height:16px;background:var(--red)}

  .badge{position:absolute;right:14px;bottom:28px;width:50px;height:50px;background:var(--badge);z-index:1}

  .facts{width:118px;height:100%;border-left:1px solid var(--panel-line);background:var(--white);padding:10px 7px;font-size:7px;line-height:1.3;color:var(--ink)}
  .facts-use{margin-bottom:6px}
  .facts-head{font-family:"Oswald",sans-serif;font-weight:600;font-size:15px;border-bottom:3px solid var(--ink);padding-bottom:2px}
  .facts-row{border-bottom:.5px solid var(--panel-line);padding:3px 0}
  .facts-row--thick{border-bottom:2px solid var(--ink)}
  .facts-foot{margin-top:6px}
</style>
</head>
<body>

<section class="label label--bone">
  <div class="front">
    <div class="top-band layer"><span class="product-line">Vitamin D3+ Quercetinol</span></div>
    <div class="brand layer"><span class="brand-name">Verdanta</span></div>
    <p class="tagline layer">Your secret beauty ingredients</p>
    <h2 class="title layer">MORNING CORE MATERNA<br>&amp; AFTERCARE</h2>
    <p class="subtitle layer">–WITH PROBIOTICS–</p>
    <p class="claims layer">VEGETARIAN / GLUTEN FREE / SOY FREE</p>
    <span class="pill layer">60 CAPSULES</span>
    <p class="bone-claim layer">A DIETARY SUPPLEMENT TO SUPPORT<br>HEALTHY BONE MINERAL DENSITY*</p>
    <div class="base-wash"></div>
  </div>
</section>

<section class="label label--hair">
  <div class="front">
    <div class="top-band layer">
      <span class="product-line">MANE FOCUS™</span>
      <span class="advert-line">Shine, renewal, Blooming</span>
    </div>
    <div class="brand layer"><span class="brand-name">Verdanta</span></div>
    <p class="tagline layer">Your secret beauty ingredients</p>
    <p class="hair-claim layer">A DIETARY SUPPLEMENT TO SUPPORT HAIR HEALTH AND GROWTH*</p>
    <p class="for-whom layer">FOR MEN &amp; WOMEN</p>
    <span class="pill layer">60 CAPSULES</span>
    <p class="diet layer">VEGETARIAN / GLUTEN FREE</p>
    <div class="base-wash"></div>
  </div>
  <aside class="facts">
    <p class="facts-use">Suggested Use: Take 2 capsules daily with food.</p>
    <p class="facts-head">Supplement Facts</p>
    <p class="facts-row">Serving Size 2 Capsules</p>
    <p class="facts-row facts-row--thick">Amount Per Serving</p>
    <p class="facts-row">Biotin 300 mcg</p>
    <p class="facts-row">Zinc 15 mg</p>
    <p class="facts-row">Copper 1 mg</p>
    <p class="facts-row">Saw Palmetto 200 mg</p>
    <p class="facts-row">Horsetail Extract 50 mg</p>
    <p class="facts-row">Grape Seed 100 mg</p>
    <p class="facts-row facts-row--thick">Bamboo Silica 40 mg</p>
    <p class="facts-foot">*Daily Value not established.</p>
    <p class="facts-foot">Other ingredients: vegetable cellulose capsule.</p>
  </aside>
</section>

<section class="label label--prenatal">
  <div class="front">
    <div class="top-band layer">
      <span class="partner-mark">CHELAMAX™</span>
      <span class="partner-note">Ironbind™ and CHELAMAX™ are trademarks of Corvell<br>Laboratories, Inc.</span>
    </div>
    <div class="brand layer"><span class="brand-name">Verdanta</span></div>
    <p class="tagline layer">Your secret beauty ingredients</p>
    <h2 class="title layer">MORNING CORE MATERNA<br>&amp; AFTERCARE</h2>
    <p class="subtitle layer">–WITH PROBIOTICS–</p>
    <p class="claims layer">A DIETARY SUPPLEMENT</p>
    <span class="pill layer">60 CAPSULES</span>
    <p class="diet layer">VEGETARIAN / GLUTEN FREE</p>
    <div class="badge" role="img" aria-label="Non-GMO certification badge"></div>
    <div class="base-wash"></div>
  </div>
  <aside class="facts">
    <p class="facts-use">Suggested Use: Take 2 capsules daily.</p>
    <p class="facts-head">Supplement Facts</p>
    <p class="facts-row">Serving Size 2 Capsules</p>
    <p class="facts-row facts-row--thick">Amount Per Serving</p>
    <p class="facts-row">Vitamin A 900 mcg</p>
    <p class="facts-row">Vitamin C 85 mg</p>
    <p class="facts-row">Vitamin D3 15 mcg</p>
    <p class="facts-row">Vitamin E 15 mg</p>
    <p class="facts-row">Thiamin 1.4 mg</p>
    <p class="facts-row">Riboflavin 1.4 mg</p>
    <p class="facts-row">Niacin 18 mg</p>
    <p class="facts-row">Folate 600 mcg</p>
    <p class="facts-row">Calcium 50 mg</p>
    <p class="facts-row">Iron 27 mg</p>
    <p class="facts-row facts-row--thick">Iodine 150 mcg</p>
  </aside>
</section>

</body>
</html>
```